redesign my woocommerce store to a minimalist and modern feel

Hi,i have a store that i quickly put together without much thought for design, here it is torvan( )dek( )ro(.) com i just knew i wanted something simple and minimalistic, our different type of logo is attached, having said that i want a complete redesign the homepage, product page, cart page, and the checkout/payment page, i want something modern and simple, i quite like how our products are displayed currently with the pictures in the homepage but that's about it, everything else is up to you.so just to recap. here is my most important conditions: the design should be minimalist, the design should support Arabic and English

Target Market(s)

Gamers

Industry/Entity Type

Games

Number of Pages Required

4 page

Font styles to use
Sans Serif

Colors

Designer to choose colors to be used in the design.

Requirements
Must have
• Simple and minimalist
• has to support 2 languages, so a drop down or a language switcher should be included in the design
Should not have
• crowded design

```html
<!DOCTYPE html>
<html lang="en">
<head>
<meta charset="utf-8">
<title>Torvandekro – Game Coins Store</title>
<link href="https://fonts.googleapis.com/css2?family=Open+Sans:wght@400;600;700&family=Varela+Round&display=swap" rel="stylesheet">
<style>
:root{
  --orange:#e9531e;
  --blue:#2a1f9e;
  --dark:#262626;
  --darker:#1b1b1b;
  --grey-bg:#f0f0f0;
  --text:#444;
  --muted:#777;
  --white:#fff;
  --line:#d6d6d6;
}
*{margin:0;padding:0;box-sizing:border-box}
html,body{width:1200px;height:4147px;overflow:hidden}
body{position:relative;font-family:"Open Sans",Arial,sans-serif;color:var(--text);background:var(--white)}
.abs{position:absolute}
.heading{font-family:"Varela Round","Open Sans",sans-serif;font-weight:400;color:var(--orange)}

/* header */
.brand{left:133px;top:18px;display:flex;align-items:center;gap:12px;font-size:38px;font-weight:700;color:var(--dark)}
.brand-dot{width:42px;height:42px;border-radius:50%;background:var(--orange)}
.lang{top:26px;display:flex;gap:10px;left:742px}
.lang span{width:30px;height:30px;border-radius:50%;background:#e6e6ee;border:1px solid #ccc}
.account{left:812px;top:34px;font-size:13px;color:var(--dark);font-weight:600;white-space:nowrap}
.cart{left:1040px;top:24px;width:36px;height:36px;border-radius:50%;background:var(--orange)}
.cart-count{left:1030px;top:18px;width:18px;height:18px;border-radius:50%;background:var(--dark);color:#fff;font-size:10px;text-align:center;line-height:18px}

.navbar{left:0;top:83px;width:1200px;height:41px;background:var(--dark)}
.menu{left:133px;top:95px;display:flex;gap:36px;font-size:14px;color:#bbb}
.menu .active{color:#fff;text-decoration:underline}
.search{left:602px;top:83px;width:598px;height:41px;background:var(--darker);color:#aaa;font-size:14px;padding:11px 30px}

/* hero */
.hero{left:0;top:124px;width:1200px;height:600px;background:var(--blue);clip-path:polygon(0 0,100% 0,100% 82%,0 100%)}
.hero-title{left:133px;top:240px;width:560px;font-size:38px;font-weight:600;color:#fff;line-height:1.3}
.hero-text{left:133px;top:352px;width:470px;font-size:16px;color:#d7d4f5;line-height:1.55}
.btn-orange{background:var(--orange);color:#fff;font-size:15px;text-align:center}
.hero-btn{left:133px;top:448px;width:124px;height:39px;line-height:39px}
.hero-art{left:636px;top:138px;width:442px;height:498px;border-radius:14px;background:radial-gradient(circle at 40% 40%,#f3c437 0 18%,#d9408f 40%,rgba(42,31,158,0) 72%)}
.arrow{font-size:40px;color:#fff}

/* features */
.feat-art{left:133px;top:802px;width:461px;height:459px;border-radius:20px;background:linear-gradient(135deg,#f7c53e 0%,#e9531e 45%,#3a4a7a 100%)}
.feat-title{left:652px;top:798px;width:430px;font-size:32px;line-height:1.25}
.feat-intro{left:652px;top:888px;width:420px;font-size:14px;color:var(--muted);line-height:1.6}
.feat-list{left:652px;top:978px;width:420px;list-style:none}
.feat-list li{display:flex;gap:20px;margin-bottom:32px;font-size:14px;font-weight:600;color:var(--dark);line-height:1.55}
.feat-list svg{flex:none;width:26px;height:26px;margin-top:4px}

/* products */
.products-bg{left:0;top:1377px;width:1200px;height:975px;background:var(--grey-bg);clip-path:polygon(0 0,100% 0,100% 100%,0 92%)}
.products-title{left:133px;top:1448px;font-size:34px}
.sort{left:838px;top:1462px;font-size:13px;color:var(--dark)}
.sort-box{left:893px;top:1449px;width:174px;height:44px;background:#fff;border:1px solid var(--line);font-size:13px;padding:12px 16px;color:var(--muted)}
.sort-box:after{content:"";position:absolute;right:16px;top:19px;border:5px solid transparent;border-top-color:#555}
.card{width:216px;text-align:center}
.card-img{height:160px;background:#fff;border:1px solid #e2e2e2}
.card-name{font-size:20px;color:var(--dark);margin-top:12px}
.card-price{font-size:11px;color:#555;margin-top:4px}
.card-btn{display:inline-block;margin-top:10px;width:82px;height:33px;line-height:31px;border:1px solid #bbb;font-size:11px;color:#666}
.btn-dark{background:#333;color:#fff;font-size:15px;text-align:center}
.view-all{left:547px;top:2132px;width:106px;height:41px;line-height:41px}

/* about */
.about-title{left:133px;top:2430px;width:470px;font-size:33px;line-height:1.25}
.about-text{left:133px;top:2522px;width:420px;font-size:14px;line-height:1.7;color:#555}
.read-more{left:133px;top:2740px;width:108px;height:42px;line-height:42px}
.laptop-screen{left:608px;top:2466px;width:416px;height:280px;border:10px solid #222;border-radius:12px 12px 0 0;background:linear-gradient(160deg,#eef1f6,#c9d6e8)}
.laptop-base{left:565px;top:2742px;width:502px;height:16px;background:linear-gradient(#bfc3c8,#8c9096);border-radius:0 0 14px 14px}

/* reviews */
.reviews-bg{left:0;top:2881px;width:1200px;height:507px;background:var(--grey-bg);clip-path:polygon(0 0,100% 0,100% 76%,0 100%)}
.reviews-title{left:0;width:1200px;top:2948px;text-align:center;font-size:36px}
.quote{top:3017px;width:296px;height:121px;background:#fff;border:1px solid #bbb;font-size:15px;text-align:center;padding:24px 20px;line-height:1.5;color:#555}
.quote:after{content:"";position:absolute;left:138px;bottom:-11px;width:20px;height:20px;background:#fff;border-right:1px solid #bbb;border-bottom:1px solid #bbb;transform:rotate(45deg)}
.reviewer{top:3168px;width:296px;text-align:center;font-size:16px;font-weight:700;color:var(--dark)}
.arrow-grey{font-size:36px;color:#aaa}

/* payments */
.pay-title{left:0;width:1200px;top:3484px;text-align:center;font-size:36px}
.pay{top:3562px;width:160px;text-align:center;font-size:26px;font-weight:700}

/* newsletter */
.news-bg{left:0;top:3733px;width:1200px;height:414px;background:var(--grey-bg)}
.news-title{left:0;width:1200px;top:3788px;text-align:center;font-size:36px}
.news-input{left:395px;top:3852px;width:291px;height:41px;background:#fff;border:1px solid var(--line);font-size:12px;color:#888;padding:12px 20px}
.news-btn{left:686px;top:3852px;width:122px;height:41px;line-height:41px;font-weight:700;font-size:15px}

/* footer */
.footer{left:0;top:3926px;width:1200px;height:221px;background:var(--dark);clip-path:polygon(0 38%,100% 0,100% 100%,0 100%)}
.foot-links{left:133px;top:4062px;font-size:12px;color:#ccc}
.foot-copy{left:133px;top:4092px;font-size:12px;color:#aaa}
.social{top:4076px;width:16px;height:16px;border-radius:50%;background:#9a9a9a}
</style>
</head>
<body>

<header>
  <div class="abs brand"><span class="brand-dot"></span>Torvandekro</div>
  <div class="abs lang" aria-label="Language switcher: English, Arabic"><span></span><span></span></div>
  <div class="abs account">My Account &nbsp;|&nbsp; My Cart - ($00.00)</div>
  <div class="abs cart" aria-label="Cart"></div>
  <div class="abs cart-count">0</div>
</header>

<nav>
  <div class="abs navbar"></div>
  <div class="abs menu"><span class="active">Home</span><span>About Us</span><span>Features</span><span>News</span><span>Contact us</span></div>
  <div class="abs search">Search
    <svg style="position:absolute;right:40px;top:13px" width="15" height="15" viewBox="0 0 16 16"><circle cx="6.5" cy="6.5" r="5" fill="none" stroke="#ddd" stroke-width="2"/><path d="M10.5 10.5L15 15" stroke="#ddd" stroke-width="2"/></svg>
  </div>
</nav>

<section class="hero-section">
  <div class="abs hero"></div>
  <h1 class="abs hero-title">Vestibulum condimentum<br>risus posuere</h1>
  <p class="abs hero-text">Etiam mattis augue vehicula odio posuere, sit amet tempus lectus luctus. Nulla facilisi. Etiam vel massa elementum, bibendum tellus venenatis, feugiat massa.</p>
  <div class="abs btn-orange hero-btn">Get Started</div>
  <div class="abs hero-art" role="img" aria-label="Illustration of a smartphone with a game, coins and a gamer on a sofa"></div>
  <div class="abs arrow" style="left:44px;top:340px">&#8249;</div>
  <div class="abs arrow" style="left:1128px;top:340px">&#8250;</div>
</section>

<section class="features">
  <div class="abs feat-art" role="img" aria-label="Illustration of a game controller, a phone and gold coins"></div>
  <h2 class="abs heading feat-title">Maecenas tortor accumsan quam varius imperdiet</h2>
  <p class="abs feat-intro">Pellentesque convallis molestie enim sit amet efficitur. Etiam id imperdiet lectus. Vivamus lacus justo, ultrices nec erat</p>
  <ul class="abs feat-list">
    <li><svg viewBox="0 0 24 24"><circle cx="12" cy="7" r="5" fill="#222"/><path d="M2 23c0-6 4-9 10-9s10 3 10 9z" fill="#222"/></svg>Nullam lorem urna, tempus eget mollis et, dapibus ac sem. Suspendisse gravida ornare erat.</li>
    <li><svg viewBox="0 0 24 24"><path d="M12 1L3 5v6c0 6 4 10 9 12 5-2 9-6 9-12V5z" fill="#222"/><path d="M12 4v16c3-1.5 6-4.5 6-9V7z" fill="#fff"/></svg>Fusce nec ac urna pulvinar auctor. Mauris bibendum fringilla velit. Nulla in lorem at massa pellentesque</li>
    <li><svg viewBox="0 0 24 24"><rect x="4" y="10" width="16" height="13" fill="#222"/><path d="M7 10V7a5 5 0 0110 0v3" fill="none" stroke="#222" stroke-width="2.5"/></svg>Etiam quis aliquet risus. Duis ornare erat eget magna dapibus, in accumsan quam pharetra.</li>
    <li><svg viewBox="0 0 24 24"><rect x="1" y="4" width="22" height="16" rx="2" fill="#222"/><rect x="1" y="8" width="22" height="3" fill="#fff"/><rect x="4" y="14" width="6" height="2" fill="#fff"/></svg>Nam tempus, quam in bibendum vulputate, sapien dolor viverra nisl, vitae euismod elit turpis.</li>
  </ul>
</section>

<section class="products">
  <div class="abs products-bg"></div>
  <h2 class="abs heading products-title">Our Product</h2>
  <div class="abs sort">Sort By :</div>
  <div class="abs sort-box">All</div>

  <div class="abs card" style="left:133px;top:1532px"><div class="card-img" role="img" aria-label="Lumo app logo" style="background:linear-gradient(135deg,#fff,#e6f3fa)"></div><div class="card-name">Lumo</div><div class="card-price">Buy 10 coin for $30</div><span class="card-btn">BUY NOW</span></div>
  <div class="abs card" style="left:373px;top:1532px"><div class="card-img" role="img" aria-label="Pixo app logo" style="background:linear-gradient(135deg,#fff,#f6e7f8)"></div><div class="card-name">Pixo</div><div class="card-price">Buy 8 coin for $25</div><span class="card-btn">BUY NOW</span></div>
  <div class="abs card" style="left:611px;top:1532px"><div class="card-img" role="img" aria-label="Brava game logo" style="background:linear-gradient(135deg,#fff,#f5ead8)"></div><div class="card-name">Brava</div><div class="card-price">Buy 15 coin for $32</div><span class="card-btn">BUY NOW</span></div>
  <div class="abs card" style="left:849px;top:1532px"><div class="card-img" role="img" aria-label="Tiki Tiki app logo" style="background:linear-gradient(135deg,#2a0a24,#7a1560)"></div><div class="card-name">Tiki Tiki</div><div class="card-price">Buy 5 coin for $15</div><span class="card-btn">BUY NOW</span></div>

  <div class="abs card" style="left:133px;top:1822px"><div class="card-img" role="img" aria-label="Aliquam product logo" style="background:radial-gradient(circle,#f4eadc 0 16%,#fff 30%)"></div><div class="card-name">Aliquam</div><div class="card-price">Buy 25coin for $40</div><span class="card-btn">BUY NOW</span></div>
  <div class="abs card" style="left:373px;top:1822px"><div class="card-img" role="img" aria-label="Vestibulum product logo" style="background:radial-gradient(circle,#e3f2e8 0 16%,#fff 30%)"></div><div class="card-name">Vestibulum</div><div class="card-price">Buy 15coin for $35</div><span class="card-btn">BUY NOW</span></div>
  <div class="abs card" style="left:611px;top:1822px"><div class="card-img" role="img" aria-label="Fusce product logo" style="background:radial-gradient(circle,#fbe5d8 0 16%,#fff 30%)"></div><div class="card-name">Fusce</div><div class="card-price">Buy 5 coin for $10</div><span class="card-btn">BUY NOW</span></div>
  <div class="abs card" style="left:849px;top:1822px"><div class="card-img" role="img" aria-label="Etiam product logo" style="background:radial-gradient(circle,#fbe3d3 0 16%,#fff 30%)"></div><div class="card-name">Etiam</div><div class="card-price">Buy 20 coin for $60</div><span class="card-btn">BUY NOW</span></div>

  <div class="abs btn-dark view-all">View All</div>
</section>

<section class="about">
  <h2 class="abs heading about-title">Etiam vel massa elementum, bibendum tellus venenatis.</h2>
  <p class="abs about-text">Aliquam erat volutpat. Quisque aliquet ex nec est vestibulum pulvinar. Pellentesque convallis molestie enim sit amet efficitur. Etiam id imperdiet lectus. Vivamus lacus justo, ultrices nec erat in, maximus iaculis mauris. Vivamus eleifend vitae nulla vel malesuada. In ac malesuada lacus, et consectetur ante. Fusce vitae lectus sit amet mi pulvinar maximus. Aenean placerat, nibh vel accumsan aliquet, magna nibh accumsan nibh.</p>
  <div class="abs btn-dark read-more">Read More</div>
  <div class="abs laptop-screen" role="img" aria-label="Laptop showing a sales dashboard with charts"></div>
  <div class="abs laptop-base"></div>
</section>

<section class="reviews">
  <div class="abs reviews-bg"></div>
  <h2 class="abs heading reviews-title">Reviews</h2>
  <div class="abs arrow-grey" style="left:36px;top:3056px">&#8249;</div>
  <div class="abs arrow-grey" style="left:1142px;top:3056px">&#8250;</div>
  <div class="abs quote" style="left:133px">"Aliquam consectetur orci molestie dictum molestie. Proin eget congue nulla, vel"</div>
  <div class="abs quote" style="left:453px">"Vestibulum condimentum, risus ut posuere cursus, velit justo accumsan"</div>
  <div class="abs quote" style="left:769px">"Pellentesque a imperdiet dolor, et auctor est. Fusce sollicitudin lorem et luctus volutpat"</div>
  <div class="abs reviewer" style="left:133px">- John Cole</div>
  <div class="abs reviewer" style="left:453px">- Sophia</div>
  <div class="abs reviewer" style="left:769px">- Daniel</div>
</section>

<section class="payments">
  <h2 class="abs heading pay-title">Secured Payments</h2>
  <div class="abs pay" style="left:170px;color:#1a2a8a">Payvo</div>
  <div class="abs pay" style="left:404px;color:#d3201e">Cardix</div>
  <div class="abs pay" style="left:634px;color:#1e8a4a">Nuqta</div>
  <div class="abs pay" style="left:869px;color:var(--orange)">Wasl</div>
</section>

<section class="newsletter">
  <div class="abs news-bg"></div>
  <h2 class="abs heading news-title">Newsletter Sign Up</h2>
  <div class="abs news-input">Email Address</div>
  <div class="abs btn-orange news-btn">SUBSCRIBE</div>
</section>

<footer>
  <div class="abs footer"></div>
  <div class="abs foot-links">Home &nbsp;|&nbsp; About Us &nbsp;|&nbsp; Features &nbsp;|&nbsp; News &nbsp;|&nbsp; Contact us</div>
  <div class="abs foot-copy">Copyright © 2018 Torvandekro . All rights reserved.</div>
  <div class="abs social" style="left:1005px" aria-label="Social link"></div>
  <div class="abs social" style="left:1048px" aria-label="Social link"></div>
</footer>

</body>
</html>
```